Pillow Company needs Pillow Insert Design

I just started a new pillow line with two pillow types. I have a hotel pillow and an organic pillow. I need two pillow insert signs designed that follow the same layout but are different color types. I want one sign to incorporate silver and white look and another sign to incorporate a green and white look (this one to look organic). They must have the same layout but different colors. I have include examples of what I want it to look like. In addition, I have uploaded the two hi res images for each sign. My logo is uploaded too.

I am open to other concepts and colors as long as it looks modern, clean and upscale. In addition, I need a Made in the USA logo on the pillow insert designs.

I have attached details on sign, images to be used, and examples that I like.

The Pillow Sign Size is 12 inches x 12 inches.

```html
<!DOCTYPE html>
<html lang="en">
<head>
<meta charset="utf-8">
<title>Restwell Luxurious Pillow Insert</title>
<link href="https://fonts.googleapis.com/css2?family=Open+Sans:wght@400;600;700&family=Pinyon+Script&display=swap" rel="stylesheet">
<style>
  :root {
    --page: #ffffff;
    --cream: #f3f2c8;
    --cream-light: #fbfbe6;
    --green: #5e9e2c;
    --green-light: #8cc43e;
    --green-dark: #2f7a2a;
    --box: #4f8a25;
    --ink: #1e1e1e;
    --muted: #444444;
    --yellow: #f2ee5a;
    --photo-a: #c9b8a8;
    --photo-b: #e9e4de;
    --badge-blue: #1f3c88;
  }
  * { margin: 0; padding: 0; box-sizing: border-box; }
  html, body { width: 1200px; height: 1000px; overflow: hidden; background: var(--page); }
  .insert {
    position: absolute; left: 160px; top: 60px; width: 880px; height: 880px;
    background: #fff; box-shadow: 0 0 0 1px #e4e4e4;
    font-family: "Open Sans", Arial, sans-serif; overflow: hidden;
  }
  .header {
    position: absolute; left: 0; top: 0; width: 880px; height: 115px;
    background: linear-gradient(90deg, var(--cream), var(--cream-light));
    display: flex; align-items: center; padding-left: 50px; gap: 20px;
  }
  .brand-mark { width: 58px; height: 58px; background: var(--green-light); }
  .brand-name { font-size: 38px; font-weight: 600; color: var(--green); }
  .side {
    position: absolute; left: 0; top: 115px; width: 347px; height: 765px;
    background: radial-gradient(circle at 40% 30%, var(--green-light), var(--green) 75%);
    color: #fff;
  }
  .title {
    font-family: "Pinyon Script", cursive; font-size: 74px; line-height: 0.95;
    color: #fff; padding: 35px 0 0 30px;
  }
  .title span { display: block; padding-left: 100px; }
  .intro {
    margin: 22px 22px 0 22px; font-size: 13px; font-weight: 700; line-height: 1.45;
    color: var(--yellow); text-transform: uppercase;
  }
  .feature-box {
    margin: 24px 0 0 0; padding: 18px 22px; background: var(--box);
    font-size: 13.5px; font-weight: 600; line-height: 1.5; text-align: center; color: #fff;
  }
  .feature-box em { font-style: normal; color: var(--yellow); }
  .benefits { list-style: none; margin: 20px 0 0 22px; }
  .benefits li {
    position: relative; padding-left: 24px; font-size: 12.5px; font-weight: 700;
    line-height: 1.45; margin-bottom: 8px; color: var(--yellow);
  }
  .benefits li::before {
    content: ""; position: absolute; left: 0; top: 4px; width: 11px; height: 11px;
    border: 1.5px solid var(--yellow);
  }
  .photo {
    position: absolute; left: 347px; top: 115px; width: 533px; height: 765px;
    background: linear-gradient(180deg, var(--photo-a) 0%, var(--photo-b) 40%, #f7f7f7 62%, #fff 78%);
  }
  .tagline {
    position: absolute; left: 360px; top: 655px; width: 520px;
    font-family: "Pinyon Script", cursive; font-size: 42px; color: var(--green-dark);
    transform: rotate(-4deg); white-space: nowrap;
  }
  .origin {
    position: absolute; left: 505px; top: 770px; font-size: 15px; line-height: 1.35; color: var(--muted);
  }
  .usa-badge { position: absolute; left: 735px; top: 745px; }
</style>
</head>
<body>
  <section class="insert">
    <header class="header">
      <div class="brand-mark"></div>
      <div class="brand-name">Restwell</div>
    </header>

    <aside class="side">
      <h1 class="title">Luxurious<span>Pillow</span></h1>
      <p class="intro">This pillow was designed to give you the most comfortable night's sleep in your life. Designed for all types of sleep positions.</p>
      <p class="feature-box">We added revolutionary features from our advanced Super Soft Premium Memory Foam that has an open cell structure design that recovers quickly and does not trap heat to our gel infused polyester fiber to our <em>100% Certified Organic Cotton Fabric.</em></p>
      <ul class="benefits">
        <li>Made From the Finest Premium Materials</li>
        <li>Adjusts to your Body Weight and Temperature</li>
        <li>100% Certified Organic Cotton Fabric</li>
        <li>Cool Non-Allergenic, Anti-Microbial, and Hypoallergenic</li>
        <li>Conforms to Head and Neck for optimal Alignment during Sleep</li>
        <li>Mildew Proof and Dust Mite Resistant</li>
        <li>PureFoam toxin free certified foam</li>
      </ul>
    </aside>

    <div class="photo" role="img" aria-label="Photo of a smiling family of three relaxing together in a bed with white bedding"></div>

    <p class="tagline">Surround yourself with the Best!</p>
    <p class="origin">Individually Handcrafted<br>and Made in USA</p>
    <svg class="usa-badge" width="120" height="120" viewBox="0 0 120 120" aria-hidden="true">
      <circle cx="60" cy="60" r="56" fill="var(--badge-blue)"/>
    </svg>
  </section>
</body>
</html>
```